URGENT Conference Banner ad to attract a crowd!

I need please in my brand colours 2 x static ads with this copy please:
Have an online business?
Make your customers stick!
It really needs to stand out but not be offensive.
I would like to see blue background on white font and then the reverse. on the white one, it needs a thin blue border around it.
I need it in static: 300x250 and 300x600.
on this one - 300x600. please add a circle saying register now!
Please see examples of other messages I have done. I need this URGENTLY pelase :)
Target Market(s)
http://www.tradefairvaltrona.com.au/en/home/
Industry/Entity Type
Business
Font styles to use
Other font styles liked:
- roboto font
Requirements
Must have
- Use this blue:
- 00b6ce
- roboto font
Nice to have
- look and feel like my banners supplied

```html
<!DOCTYPE html>
<html lang="en">
<head>
<meta charset="utf-8">
<title>Have an online business? – Banner 300x250</title>
<link rel="stylesheet" href="https://fonts.googleapis.com/css2?family=Roboto:wght@300;700&display=swap">
<style>
  :root {
    --brand-blue: #00c1d7;
    --text-white: #ffffff;
    --page-bg: #ffffff;
    --icon-tone: #e3f8fb;
  }
  html, body {
    margin: 0;
    padding: 0;
    width: 1200px;
    height: 1000px;
    overflow: hidden;
    background: var(--page-bg);
  }
  .canvas {
    position: relative;
    width: 1200px;
    height: 1000px;
  }
  .banner {
    position: absolute;
    left: 453px;
    top: 382px;
    width: 300px;
    height: 250px;
    background: var(--brand-blue);
    color: var(--text-white);
    font-family: "Roboto", Arial, sans-serif;
    overflow: hidden;
  }
  .headline {
    position: absolute;
    left: 19px;
    top: 14px;
    margin: 0;
    font-size: 33px;
    font-weight: 700;
    line-height: 39px;
    letter-spacing: 0;
    text-transform: uppercase;
    white-space: nowrap;
  }
  .tagline {
    position: absolute;
    left: 19px;
    top: 147px;
    margin: 0;
    font-size: 33px;
    font-weight: 300;
    line-height: 39px;
    letter-spacing: 0;
    white-space: nowrap;
  }
  .payment-icon {
    position: absolute;
    left: 200px;
    top: 20px;
    width: 90px;
    height: 132px;
  }
</style>
</head>
<body>
  <main class="canvas">
    <section class="banner">
      <h1 class="headline">Have an<br>online<br>business?</h1>
      <p class="tagline">Make your<br>customers stick!</p>
      <svg class="payment-icon" viewBox="0 0 90 132" role="img" aria-label="Icon of a hand tapping a card with a dollar sign">
        <rect x="2" y="2" width="86" height="128" rx="12" fill="var(--icon-tone)"/>
      </svg>
    </section>
  </main>
</body>
</html>
```